Letterhead Design Project

Standard A4 paper, center the name Brightway Wash (with the mop) same as front of business card.
47 Harbour Vale Rd Kelston 5062 ABN: 71205839416
M. 0427163958 T. 83917605 Calibri font

Industry/Entity Type

Business

```html
<!DOCTYPE html>
<html lang="en">
<head>
<meta charset="utf-8">
<title>Brightway Wash Letterhead</title>
<link rel="stylesheet" href="https://fonts.googleapis.com/css2?family=Carlito:wght@400;700&display=swap">
<style>
  :root {
    --backdrop: #232e3a;
    --paper: #ffffff;
    --royal-blue: #1a2fbf;
    --sky-blue: #6a96f2;
    --ink-grey: #4a4a4a;
  }
  * { margin: 0; padding: 0; box-sizing: border-box; }
  html, body {
    width: 992px;
    height: 1200px;
    overflow: hidden;
    background: var(--backdrop);
  }
  .canvas {
    position: relative;
    width: 992px;
    height: 1200px;
  }
  .letterhead {
    position: absolute;
    left: 106px;
    top: 48px;
    width: 780px;
    height: 1103px;
    background: var(--paper);
    font-family: "Carlito", "Calibri", sans-serif;
    box-shadow: 0 6px 18px rgba(0, 0, 0, 0.45);
    overflow: hidden;
  }
  .corner-swoosh {
    position: absolute;
    inset: 0;
    width: 780px;
    height: 1103px;
  }
  .brand {
    position: absolute;
    right: 50px;
    top: 112px;
  }
  .brand-name {
    font-weight: 700;
    font-size: 44px;
    letter-spacing: 0.5px;
    color: var(--royal-blue);
  }
  .header-rule {
    position: absolute;
    left: 300px;
    right: 50px;
    top: 196px;
    height: 3px;
    background: linear-gradient(to right, rgba(26, 47, 191, 0), var(--royal-blue));
  }
  .footer-rule {
    position: absolute;
    left: 50px;
    width: 400px;
    top: 884px;
    height: 3px;
    background: linear-gradient(to right, var(--royal-blue), rgba(26, 47, 191, 0));
  }
  .contact-details {
    position: absolute;
    left: 50px;
    top: 898px;
    list-style: none;
    font-size: 16px;
    line-height: 21px;
    color: var(--ink-grey);
  }
</style>
</head>
<body>
  <main class="canvas">
    <section class="letterhead">
      <svg class="corner-swoosh" viewBox="0 0 780 1103" aria-hidden="true">
        <rect width="780" height="1103" fill="var(--royal-blue)"/>
        <ellipse cx="390" cy="551" rx="800" ry="520" transform="rotate(-55 390 551)" fill="var(--sky-blue)"/>
        <ellipse cx="390" cy="551" rx="760" ry="462" transform="rotate(-55 390 551)" fill="var(--paper)"/>
      </svg>

      <header class="brand">
        <span class="brand-name">Brightway Wash</span>
      </header>
      <div class="header-rule"></div>

      <div class="footer-rule"></div>
      <ul class="contact-details">
        <li>47 Harbour Vale Rd Kelston 5062</li>
        <li>ABN: 71205839416</li>
        <li>Mobile: 0427163958</li>
        <li>Tel: 83917605</li>
      </ul>
    </section>
  </main>
</body>
</html>
```